Vital Spark Electrical in need of a business card design

We need a new business card designed for our electrical business. We have a logo already which I will attach below.
Would like the business card to be..
-BLACK background preferably, possibly white back ground behind logo if colours clash.
-White & Blue (logo blue) text
Something that makes the logo pop, & a modern look. Possibly minimal clean format.

REQUIRE:
-Logo on front & back

TEXT TO INCLUDE (ON ONE SIDE):

Tom Harlow
Director/Electrician
M: 0417 365 208
E:info@vitalsparkelectrical-example.com.au
W:www.vitalsparkelectrical-example.com.au
R.E.C 57318

Custom/New Homes
Renovations
Commercial Office/Shop Fit-outs
Communications & Security Cameras
Electric Vehicle Chargers
Airconditioning
Updates

Requirements
Nice to have
• Possibly even lighten the grey shades for the words 'Vital' & 'Spark' to be more easily read on a black background.

```html
<!DOCTYPE html>
<html lang="en">
<head>
<meta charset="utf-8">
<title>Vital Spark Electrical — Business Card Back</title>
<link href="https://fonts.googleapis.com/css2?family=Montserrat:wght@300;600&display=swap" rel="stylesheet">
<style>
  :root {
    --paper: #ffffff;
    --slate: #313e48;
    --ink: #2f3d48;
    --spark-blue: #06a9e2;
    --service-grey: #a0a7ad;
  }
  html, body {
    margin: 0;
    padding: 0;
    width: 1200px;
    height: 686px;
    overflow: hidden;
    background: var(--paper);
  }
  .card {
    position: relative;
    width: 1200px;
    height: 686px;
    font-family: "Montserrat", sans-serif;
  }
  .brand-area {
    position: absolute;
    left: 0;
    top: 0;
    width: 1200px;
    height: 278px;
    background: var(--paper);
    display: flex;
    align-items: center;
    justify-content: center;
    gap: 18px;
  }
  .brand-square {
    width: 38px;
    height: 38px;
    background: var(--spark-blue);
  }
  .brand-name {
    margin: 0;
    font-weight: 600;
    font-size: 36px;
    letter-spacing: 0.5px;
    color: var(--ink);
  }
  .services-band {
    position: absolute;
    left: 0;
    top: 278px;
    width: 1200px;
    height: 408px;
    background: var(--slate);
  }
  .services-list {
    list-style: none;
    margin: 0;
    padding: 0;
    position: absolute;
    top: 68px;
    left: 0;
    width: 100%;
    text-align: center;
  }
  .services-list li {
    font-weight: 300;
    font-size: 30px;
    line-height: 43px;
    letter-spacing: 0.6px;
    color: var(--service-grey);
  }
</style>
</head>
<body>
  <div class="card">
    <header class="brand-area">
      <span class="brand-square" aria-hidden="true"></span>
      <h1 class="brand-name">Vital Spark Electrical</h1>
    </header>
    <section class="services-band">
      <ul class="services-list">
        <li>Custom/New Homes</li>
        <li>Renovations</li>
        <li>Commercial Office/Shop Fit-outs</li>
        <li>Communications &amp; Security Cameras</li>
        <li>Electric Vehicle Chargers</li>
        <li>Airconditioning</li>
      </ul>
    </section>
  </div>
</body>
</html>
```